We need a small, simple graphic for the company newsletter. The topic of this issue is voting. As a company, we believe it is important to vote; therefore, we're going to explain the importance of voting, how to vote, when to vote, and how the company will be providing time off to vote. We would like the graphic to be simple (2-3 colors) and look like the sticker or pin you received after voting that says "I voted". We would like our company logo incorporated somehow, so be creative. It must contain our company color of blue (r 38, g 58, b 128). The company logo is attached, as well as some I voted stickers for reference

Requirements
Must have
• Use our company color of blue (r 38 g 58 b 128). Use the words "I Voted". Use the company font Bebas and/or Helvetica Neue. The background must be white as it will be incorporated into a newsletter document.
Nice to have
• Incorporate the company logo. American flag
Should not have
• fireworks, reference to 2020

```html
<!DOCTYPE html>
<html lang="en">
<head>
<meta charset="utf-8">
<title>I Voted — Newsletter Graphic</title>
<link rel="stylesheet" href="https://fonts.googleapis.com/css2?family=Bebas+Neue&family=Roboto:wght@500&display=swap">
<style>
  :root {
    --company-blue: #263a80;
    --check-red: #dc222b;
    --frame-grey: #a7a9ac;
    --paper: #ffffff;
    --flag-navy: #1f2d63;
    --flag-red: #b3121f;
    --flag-white: #f2f2f2;
  }
  html, body {
    margin: 0;
    padding: 0;
    width: 1200px;
    height: 876px;
    overflow: hidden;
    background: var(--paper);
  }
  .sticker {
    position: relative;
    width: 1200px;
    height: 876px;
    background: var(--paper);
  }
  .headline {
    position: absolute;
    left: 0;
    top: 0;
    width: 1200px;
    height: 600px;
  }
  .headline__text {
    font-family: "Bebas Neue", "Helvetica Neue", Arial, sans-serif;
    font-size: 441px;
    fill: var(--company-blue);
  }
  .headline__letter { fill: var(--company-blue); }
  .headline__check { fill: var(--check-red); }

  .banner {
    position: absolute;
    top: 606px;
    height: 185px;
  }
  .banner--stars {
    left: 82px;
    width: 376px;
    background: linear-gradient(120deg, var(--flag-navy) 0%, #2c3f86 55%, #34488f 100%);
  }
  .banner--stripes {
    left: 737px;
    width: 371px;
    background: linear-gradient(150deg, var(--flag-red) 0%, #e23038 30%, var(--flag-white) 55%, #9c1a22 80%, var(--flag-white) 100%);
  }
  .brand-box {
    position: absolute;
    left: 471px;
    top: 609px;
    width: 251px;
    height: 184px;
    box-sizing: border-box;
    border: 2px solid var(--frame-grey);
    display: flex;
    align-items: center;
    justify-content: center;
    gap: 10px;
  }
  .brand-box__mark {
    width: 18px;
    height: 18px;
    background: var(--company-blue);
  }
  .brand-box__name {
    font-family: "Roboto", "Helvetica Neue", Arial, sans-serif;
    font-size: 28px;
    font-weight: 500;
    line-height: 1;
    color: var(--company-blue);
    margin: 0;
  }
</style>
</head>
<body>
  <main class="sticker">
    <svg class="headline" viewBox="0 0 1200 600" role="img" aria-label="I Voted">
      <rect class="headline__letter" x="80" y="252" width="68" height="308"/>
      <polygon class="headline__letter" points="215,252 289,252 352,430 315,560"/>
      <polygon class="headline__check" points="450,83 524,83 392,560 315,560"/>
      <text class="headline__text" x="477" y="564" textLength="635" lengthAdjust="spacingAndGlyphs">OTED</text>
    </svg>

    <div class="banner banner--stars" role="img" aria-label="Waving American flag, blue field with white stars"></div>

    <div class="brand-box">
      <span class="brand-box__mark"></span>
      <p class="brand-box__name">Harwick Group</p>
    </div>

    <div class="banner banner--stripes" role="img" aria-label="Waving American flag, red and white stripes"></div>
  </main>
</body>
</html>
```